Business Card Design for Cybersecurity Company - Quorvent Systems

We need a business card design for our new cybersecurity company, Quorvent. We’re going for a clean, hi tech look that feels modern, premium, and trustworthy. We want a design that really stands out and makes people say WOW when we hand it over!

Quorvent delivers reliable IT support and managed services for small and mid sized businesses. We help companies stay secure, efficient, and connected through proactive monitoring, cybersecurity services, cloud management, and remote support.

Target Market(s)

Designers should target small and mid sized businesses that need dependable cybersecurity and IT support.

Industry/Entity Type

Cybersecurity, Managed Service Provider, IT services

Contact Information for Business Card

Contact information

Requirements
Must have
• The card should look clean, modern, and tech focused, with the Quorvent logo, clear contact info, and strong readability. It needs to feel premium and professional while still keeping a simple layout that fits a cybersecurity and IT brand.
Nice to have
• Nice to have elements include subtle touches that give the card a modern, tech feel, along with a layout that works well in different background styles.
Should not have
• The card should avoid clutter, loud graphics, or anything that takes attention away from the logo and contact details.

```html
<!DOCTYPE html>
<html lang="en">
<head>
<meta charset="UTF-8">
<title>Quorvent Systems — Business Card</title>
<link href="https://fonts.googleapis.com/css2?family=Figtree:wght@400;600&display=swap" rel="stylesheet">
<style>
  :root {
    --page: #ffffff;
    --card: #000000;
    --ink: #f2f2f2;
    --glow-blue: rgba(52, 92, 240, 0.95);
    --glow-violet: rgba(120, 40, 230, 0.95);
    --glow-magenta: rgba(160, 20, 220, 0.95);
  }
  * { margin: 0; padding: 0; box-sizing: border-box; }
  html, body {
    width: 1032px;
    height: 1200px;
    overflow: hidden;
    background: var(--page);
    font-family: "Figtree", sans-serif;
    color: var(--ink);
  }
  .sheet {
    position: relative;
    width: 1032px;
    height: 1200px;
  }
  .card {
    position: absolute;
    top: 478px;
    width: 376px;
    height: 243px;
    background: var(--card);
    overflow: hidden;
  }
  .card--front { left: 120px; }
  .card--back { left: 536px; }

  .glow { position: absolute; inset: 0; }
  .card--front .glow {
    background:
      radial-gradient(ellipse 60px 40px at 60px 215px, var(--glow-blue), transparent 100%),
      radial-gradient(ellipse 150px 90px at 30px 250px, var(--glow-violet), transparent 100%),
      radial-gradient(ellipse 90px 30px at 55px 250px, var(--glow-magenta), transparent 100%);
  }
  .card--back .glow {
    background:
      radial-gradient(ellipse 70px 55px at 300px 45px, var(--glow-blue), transparent 100%),
      radial-gradient(ellipse 90px 50px at 370px 0px, var(--glow-magenta), transparent 100%),
      radial-gradient(ellipse 150px 120px at 320px 20px, rgba(90, 50, 220, 0.75), transparent 100%);
  }

  .brand {
    position: absolute;
    left: 0; right: 0;
    top: 104px;
    display: flex;
    align-items: center;
    justify-content: center;
    gap: 10px;
  }
  .brand__mark {
    width: 14px;
    height: 14px;
    border-radius: 50%;
    background: var(--ink);
  }
  .brand__name {
    font-size: 22px;
    font-weight: 600;
    letter-spacing: 0.2px;
    color: var(--ink);
  }

  .contact {
    position: absolute;
    left: 27px;
    right: 31px;
    top: 114px;
    font-size: 9.6px;
    font-weight: 400;
    letter-spacing: 0.2px;
    line-height: 1.3;
  }
  .contact__name {
    font-size: 15px;
    font-weight: 600;
    letter-spacing: 0.2px;
    line-height: 1.2;
  }
  .contact__role { margin-top: 3px; }
  .contact__phones { margin-top: 17px; }
  .contact__footer {
    margin-top: 12px;
    display: flex;
    justify-content: space-between;
  }
</style>
</head>
<body>
  <main class="sheet">
    <section class="card card--front" aria-label="Card front">
      <div class="glow"></div>
      <div class="brand">
        <span class="brand__mark"></span>
        <span class="brand__name">Quorvent Systems</span>
      </div>
    </section>

    <section class="card card--back" aria-label="Card back">
      <div class="glow"></div>
      <div class="contact">
        <h1 class="contact__name">DORIAN HALE</h1>
        <p class="contact__role">Owner &amp; CEO - Quorvent Systems</p>
        <p class="contact__phones">(855) 340-QRVT<br>(813) 555-0172</p>
        <p class="contact__footer">
          <span class="contact__email">dorian@quorvent.com</span>
          <span class="contact__web">quorvent.com</span>
        </p>
      </div>
    </section>
  </main>
</body>
</html>
```